In Home Senior Care Agency Business Card Design Needed

At Silver Birch Helpers, we don't just work in the care-giving industry. We truly care.

We are dedicated to providing personable, hands-on and integrated caring services that aim to help people maintain safe and comfortable life standards within the familiar settings of their own homes.

We would like to see designs that use my logo colors obviously. The final design will be modern, yet professional and semi-minimalistic. It should communicate an well-established company that is innovative. We would also like the design to have that 'flat' design look. Ideally having the design roll over to the backend of the card. Most likely it will be printed on a Matte paper with a die cut (either 2 rounded corners -leaf cut) or all rounded.

Target Market(s)

Baby boomer generation. 45 years and older.

Industry/Entity Type

Business

Contact Information for Business Card

Text for Front:
Slogan somewhere "Kind Hands. Caring At Home.”

Darren Holloway
President

Cell: 512.608.7719
Phone: 512.274.6051
E: Darren@silverbirchhelpers.net
W: www.SilverBirchHelpers.net

Back:
-Meal Preparation
-Transportation
-Light Housekeeping
-Bathing Assistance
-Companionship

Font styles to use
Serif
Sans Serif

Requirements
Must have
• Flat, modern, professional design. Not too many colors. Match my colors in logo. Design of card must reflect from the front onto the back. Evenly spaced font.
Nice to have
• Try to work off current logo scheme, but logo may need to be redesigned.
Should not have
• Not too many colors.

```html
<!DOCTYPE html>
<html lang="en">
<head>
<meta charset="utf-8">
<title>Silver Birch Helpers – Business Card</title>
<link href="https://fonts.googleapis.com/css2?family=Mulish:wght@400;700;800&display=swap" rel="stylesheet">
<style>
  :root {
    --bg: #e9eaea;
    --card: #ffffff;
    --green: #0a6a3a;
    --orange: #f6b33f;
    --ink: #2e2e2e;
    --ink-soft: #3a3a3a;
    --white: #ffffff;
  }
  * { box-sizing: border-box; margin: 0; padding: 0; }
  html, body {
    width: 983px; height: 1200px; overflow: hidden;
    background: var(--bg);
    font-family: "Mulish", "Century Gothic", sans-serif;
  }
  .canvas { position: relative; width: 983px; height: 1200px; }

  .card {
    position: absolute; left: 85px; width: 806px;
    background: var(--card);
    border-radius: 66px;
    overflow: hidden;
    box-shadow: 0 2px 10px rgba(0,0,0,0.12);
  }
  .card--front { top: 89px; height: 473px; }
  .card--back  { top: 640px; height: 476px; }

  .band {
    position: absolute; left: 0; right: 0; bottom: 0;
    background: var(--green);
    border-top: 9px solid var(--orange);
    display: flex; flex-direction: column; align-items: center; justify-content: center;
  }
  .card--front .band { height: 142px; gap: 14px; }
  .card--back .band { height: 143px; }

  .brand {
    position: absolute; left: 0; right: 0; top: 150px;
    display: flex; align-items: center; justify-content: center; gap: 18px;
  }
  .brand__dot { width: 30px; height: 30px; border-radius: 50%; background: var(--orange); }
  .brand__name {
    font-weight: 800; font-size: 52px; color: var(--green); letter-spacing: -0.5px;
  }

  .services { display: flex; align-items: center; color: var(--white); font-weight: 800; font-size: 23px; }
  .services__sep {
    width: 13px; height: 13px; border-radius: 50%; background: var(--orange);
    margin: 0 7px;
  }

  .contact { position: absolute; left: 87px; top: 89px; color: var(--ink-soft); }
  .contact__name { font-weight: 800; font-size: 21px; color: var(--ink); }
  .contact__title { font-size: 21px; margin-top: 8px; }
  .contact__list { list-style: none; margin-top: 20px; }
  .contact__item { display: flex; align-items: center; font-size: 21px; height: 33px; }
  .contact__icon { width: 18px; height: 18px; margin-right: 14px; flex: none; }

  .slogan { color: var(--orange); font-weight: 800; font-size: 27px; }
</style>
</head>
<body>
<div class="canvas">

  <section class="card card--front">
    <div class="brand">
      <span class="brand__dot"></span>
      <span class="brand__name">Silver Birch Helpers</span>
    </div>
    <div class="band">
      <p class="services">Meal Preparation<span class="services__sep"></span>Transportation<span class="services__sep"></span>Companionship</p>
      <p class="services">Light Housekeeping<span class="services__sep"></span>Bathing Assistance</p>
    </div>
  </section>

  <section class="card card--back">
    <div class="contact">
      <p class="contact__name">Darren Holloway</p>
      <p class="contact__title">President</p>
      <ul class="contact__list">
        <li class="contact__item">
          <svg class="contact__icon" viewBox="0 0 18 18" fill="none" stroke="#0a6a3a" stroke-width="1.6"><rect x="4" y="1.5" width="10" height="15" rx="1.5"/><line x1="7.5" y1="14" x2="10.5" y2="14"/></svg>
          512.608.7719
        </li>
        <li class="contact__item">
          <svg class="contact__icon" viewBox="0 0 18 18" fill="#0a6a3a"><path d="M4.2 1.5l3 3-1.7 2a10 10 0 0 0 6 6l2-1.7 3 3-2.2 2.2C8 15.5 2.5 10 2 3.7z"/></svg>
          512.274.6051
        </li>
        <li class="contact__item">
          <svg class="contact__icon" viewBox="0 0 18 18" fill="none" stroke="#0a6a3a" stroke-width="1.6"><rect x="1.5" y="4" width="15" height="10"/><polyline points="1.5,4 9,10 16.5,4"/></svg>
          Darren@silverbirchhelpers.net
        </li>
        <li class="contact__item">
          <svg class="contact__icon" viewBox="0 0 18 18" fill="none" stroke="#0a6a3a" stroke-width="1.4"><circle cx="9" cy="9" r="7.5"/><ellipse cx="9" cy="9" rx="3.5" ry="7.5"/><line x1="1.5" y1="9" x2="16.5" y2="9"/><line x1="9" y1="1.5" x2="9" y2="16.5"/></svg>
          www.SilverBirchHelpers.net
        </li>
      </ul>
    </div>
    <div class="band">
      <p class="slogan">“Kind Hands. Caring At Home.”</p>
    </div>
  </section>

</div>
</body>
</html>
```